KRV e-payment Business Card Design

We require a new business card design to suit our expanding consulting business -who are specialists in 2 main areas
1. Advising large Corporations and Government organisation on how to improve the why they use emerging (B2B) electronic payment systems
2. Educate Global and regional banks on how to design, build and market electronic business payment products in emerging markets

Our logo is grey/silver based with a building block theme. It also suggests "insight" and business know-how capitalizing on our KRV name. We also want to engender trust,security and balance via the ying/yan symbol

The design needs to take into account the target regional areas of Australiasia/Asia Pacific/Middle East and Africa

Target Market(s)

Regional Banks and their business customers

Industry/Entity Type

Electronic

Contact Information for Business Card

Marcus Dellwyn
Director KRV Consulting (Aust) Pty Ltd
PO Box 4736
Brambleton NSW 2164
Australia
tel +61 (0) 2 95316407
mob +61 (0) 438275601
krvconsulting@lumenpost.com

```html
<!DOCTYPE html>
<html lang="en">
<head>
<meta charset="utf-8">
<title>KRV Consulting – Business Card</title>
<link rel="stylesheet" href="https://fonts.googleapis.com/css2?family=Source+Sans+3:wght@400;600&display=swap">
<style>
  :root {
    --backdrop: #262626;
    --card: #ffffff;
    --brand-blue: #0f5891;
    --ink: #3a3a3a;
    --muted: #5a5a5a;
    --band-grey: #414141;
    --divider: #243447;
  }
  * { margin: 0; padding: 0; box-sizing: border-box; }
  html, body {
    width: 1200px; height: 999px; overflow: hidden;
    background: var(--backdrop);
    font-family: "Source Sans 3", "Myriad Pro", sans-serif;
  }
  .card {
    position: absolute; left: 75px; top: 199px;
    width: 1050px; height: 600px;
    background: var(--card);
    overflow: hidden;
  }
  .abs { position: absolute; white-space: nowrap; }

  .brand-dot {
    left: 53px; top: 205px; width: 124px; height: 124px;
    border-radius: 50%; background: var(--ink);
  }
  .brand-name {
    left: 188px; top: 180px;
    font-size: 138px; font-weight: 400; line-height: 1;
    color: var(--brand-blue); letter-spacing: -1px;
  }
  .brand-entity {
    left: 60px; top: 340px;
    font-size: 34px; color: var(--muted); line-height: 1;
  }
  .divider {
    left: 493px; top: 134px; width: 2px; height: 326px;
    background: linear-gradient(var(--card), var(--divider) 20%, var(--divider) 80%, var(--card));
  }
  .person-name {
    left: 560px; top: 118px;
    font-size: 47px; color: var(--brand-blue); line-height: 1;
  }
  .person-role {
    left: 564px; top: 175px;
    font-size: 26px; color: var(--ink); line-height: 1;
  }
  .address { left: 613px; top: 258px; font-size: 27px; color: var(--ink); line-height: 35px; }
  .contact { left: 618px; font-size: 27px; color: var(--ink); line-height: 1; }
  .contact.tel { top: 364px; }
  .contact.mob { top: 398px; }
  .contact.mail { top: 433px; }
  .icon { position: absolute; }
  .bands { position: absolute; left: 0; top: 0; }
</style>
</head>
<body>
  <main class="card">
    <span class="abs brand-dot"></span>
    <div class="abs brand-name">KRV</div>
    <div class="abs brand-entity">Consulting (Aust) Pty Ltd.</div>

    <span class="abs divider"></span>

    <h1 class="abs person-name" style="font-weight:400">Marcus Dellwyn</h1>
    <div class="abs person-role">Director</div>

    <svg class="icon" style="left:563px;top:266px" width="22" height="36" viewBox="0 0 22 36" aria-hidden="true">
      <path d="M11 0C5 0 0 5 0 11c0 8 11 25 11 25s11-17 11-25C22 5 17 0 11 0z" fill="var(--brand-blue)"/>
      <circle cx="11" cy="11" r="5" fill="#fff"/>
    </svg>
    <address class="abs address" style="font-style:normal">(Aust) Pty Ltd PO Box 4736<br>Brambleton NSW 2164 Australia</address>

    <svg class="icon" style="left:566px;top:363px" width="24" height="24" viewBox="0 0 24 24" aria-hidden="true">
      <path d="M5 2l4 4-2 3c1 3 4 6 7 7l3-2 4 4-3 4C10 21 3 14 1 5z" fill="var(--brand-blue)"/>
      <path d="M14 3a7 7 0 0 1 7 7M14 7a3 3 0 0 1 3 3" stroke="var(--brand-blue)" stroke-width="2" fill="none"/>
    </svg>
    <div class="abs contact tel">+61 (0) 2 95316407</div>

    <svg class="icon" style="left:567px;top:398px" width="22" height="24" viewBox="0 0 22 24" aria-hidden="true">
      <rect x="0" y="0" width="22" height="24" rx="4" fill="var(--brand-blue)"/>
      <rect x="5" y="4" width="12" height="14" fill="#fff"/>
      <path d="M7 15l8-9" stroke="var(--brand-blue)" stroke-width="2"/>
    </svg>
    <div class="abs contact mob">+61 (0) 438275601</div>

    <svg class="icon" style="left:567px;top:433px" width="22" height="24" viewBox="0 0 22 24" aria-hidden="true">
      <rect x="0" y="0" width="22" height="24" rx="4" fill="var(--brand-blue)"/>
      <text x="11" y="17" text-anchor="middle" font-size="15" fill="#fff" font-family="Source Sans 3, sans-serif">@</text>
    </svg>
    <div class="abs contact mail">krvconsulting@lumenpost.com</div>

    <svg class="bands" width="1050" height="600" viewBox="0 0 1050 600" aria-hidden="true">
      <rect x="0" y="536" width="620" height="30" fill="var(--band-grey)"/>
      <path d="M0 561H545C590 561 600 511 650 511H1050V600H0Z" fill="var(--brand-blue)"/>
    </svg>
  </main>
</body>
</html>
```